My portfolio needs a makeover! Clean, modern portfolio website needed for tech professional

I need a modern, updated design for my existing portfolio site (https://mirelvoss.folioplace.example/). I am a content professional who has done a lot of different types of content work for big companies. I don't really have a title.

I want to stay simple and clean, but also can be a little whimsical, fun, and a little colorful to go along with the logo I just selected.

I have a domain on Wordpress (mirelvoss.example), but I’d be willing to move my domain to another site for the right design.

I would like it coded/configured and deployed, but I need the ability to update the site myself later to easily switch out my portfolio pieces. I’m not very good at html/xml.

Pages needed:
Home page
Who I am
How to reach me
What I do > By Craft (in the nav, this will be a dropdown under What I Do)
What I do > By Brand (in the nav, this will be a dropdown under What I Do)

Please see Website Design Doc for details!

Requirements
Must have
• Design must include these pages:
1. Homepage
2. Who I Am
3. What I Do
- By Brand
- By Craft
4. How to Reach Me
Nice to have
• Example portfolio sites I like:
https://www.vornaledger.example/
http://lunadrexel.example/
https://www.tjworvan.example/
https://www.orrinbalquist.example/

For my portfolio pieces, I like either tiles or a carousel.

```html
<!DOCTYPE html>
<html lang="en">
<head>
<meta charset="utf-8">
<title>Mirel Voss — Content Everything</title>
<link rel="stylesheet" href="https://fonts.googleapis.com/css2?family=Libre+Baskerville:wght@400;700&family=Open+Sans:wght@400;600&family=Oswald:wght@700&display=swap">
<style>
:root{
  --stage:#22273a;
  --navy:#151428;
  --green:#9bc53d;
  --blue:#3aa0d8;
  --white:#ffffff;
  --ink:#1c1c24;
  --grey-text:#444;
  --hero-a:#3b3b3d;
  --hero-b:#8a8a8c;
  --map:#d6d6d6;
}
*{box-sizing:border-box;margin:0;padding:0}
html,body{width:1200px;height:5181px;overflow:hidden}
body{position:relative;background:var(--white);font-family:"Libre Baskerville",Georgia,serif;color:var(--ink)}
.abs{position:absolute}
.sans{font-family:"Open Sans",Arial,sans-serif}

/* staged area, flattened */
.stage{left:0;top:0;width:1200px;height:855px;background:var(--stage)}
.stage-name{left:0;top:95px;width:1200px;text-align:center;font-family:"Oswald",Impact,sans-serif;font-size:130px;letter-spacing:6px;color:rgba(0,0,0,.22)}
.mini-hero{left:248px;top:250px;width:704px;height:450px;background:linear-gradient(110deg,var(--hero-a),var(--hero-b));overflow:hidden}

/* hero */
.hero{left:0;top:855px;width:1200px;height:640px;background:linear-gradient(110deg,var(--hero-a) 0%,#5a5a5c 45%,var(--hero-b) 100%)}
.logo{display:flex;align-items:center;gap:10px;color:var(--blue);font-family:"Libre Baskerville",Georgia,serif;font-weight:700}
.logo .dot{width:14px;height:14px;border-radius:50%;background:var(--green)}
.nav{display:flex;gap:46px;font-family:"Open Sans",Arial,sans-serif;color:var(--white);font-size:11px}
.nav .social{width:18px;height:18px;background:var(--blue)}
.portrait{background:linear-gradient(180deg,#b88a62,#7f9cc4);}
.frame{border:2px solid rgba(255,255,255,.85)}
.frame-gap{background:inherit}
.hero-title{color:var(--white);font-size:58px;text-align:center;white-space:nowrap}
.hero-sub{color:var(--white);font-size:13px;letter-spacing:4px;text-align:center}

/* intro */
.intro-photo{left:232px;top:1655px;width:426px;height:430px;background:linear-gradient(150deg,#1a1a1a,#6d6a66 55%,#2a2a2a)}
.intro-card{left:502px;top:1563px;width:468px;height:432px;background:var(--navy);color:var(--white);padding:52px 56px}
.intro-card h2{font-size:29px;line-height:1.25;font-weight:700}
.intro-card h2 em{color:var(--blue);font-style:normal}
.intro-card p{margin-top:34px;font-size:11px;line-height:2.25}

.section-title{width:1200px;text-align:center;font-size:30px;font-weight:700;color:var(--ink)}
.section-title .hl{color:var(--green)}
.rule{height:5px;width:64px;background:var(--green)}

/* who */
.who-band{left:0;top:2315px;width:1200px;height:440px;background:var(--navy)}
.who-photo{left:152px;top:2220px;width:383px;height:630px;background:linear-gradient(160deg,#f1ebe2,#d7b28a 50%,#efe8dc)}
.who-title{left:592px;top:2396px;font-size:30px;font-weight:700;color:var(--white)}
.who-title .hl{color:var(--green)}
.who-text{left:587px;top:2483px;width:420px;color:var(--white);font-size:11px;line-height:2.35}
.arrow-box{left:978px;top:2658px;width:54px;height:54px;border:2px solid var(--white)}

/* experience */
.icon-box{width:82px;height:82px;background:var(--navy)}
.timeline{left:599px;top:3160px;width:2px;height:720px;background:#9a9a9a}
.role{height:48px;background:var(--navy);color:var(--white);font-size:18px;font-weight:700;display:flex;align-items:center;justify-content:center}
.role .hl{color:var(--green);margin-right:6px}
.step{width:56px;height:56px;background:var(--white);border:2px solid var(--ink)}
.duties{font-size:9.5px;line-height:1.85;color:var(--grey-text)}
.duties.right{text-align:right}

/* testimonials */
.voices{left:0;top:3985px;width:1200px;height:535px;background:linear-gradient(180deg,#2f2f30 0%,#4b4b4c 55%,#6a6a6b 100%)}
.voices-title{left:0;top:4100px;width:1200px;text-align:center;color:var(--white);font-size:30px;font-weight:700}
.card{top:4240px;width:300px;height:175px;padding:52px 26px 0;text-align:center;font-size:9.5px;line-height:1.8;color:#222}
.card.dim{background:#909091}
.card.lit{background:var(--white)}
.card .who{margin-top:12px;font-style:italic;font-size:13px}
.avatar{top:4205px;width:66px;height:66px;border-radius:50%;background:linear-gradient(160deg,#9aa6b2,#4e5660);border:3px solid var(--white)}
.dot{top:4466px;width:10px;height:10px;border-radius:50%;border:1.5px solid var(--white)}
.dot.on{background:var(--white)}

/* contact */
.map{top:4520px;height:661px;background:linear-gradient(135deg,#e2e2e2,#cbcbcb)}
.contact{left:380px;top:4520px;width:440px;height:661px;background:var(--navy);color:var(--white);text-align:center}
.contact h2{position:absolute;top:118px;width:100%;font-size:28px;font-weight:700}
.field{position:absolute;left:48px;width:344px;height:30px;border-bottom:1px solid #8a8a9a;text-align:left;font-size:9px;color:#d8d8e0;padding-top:10px}
.send{position:absolute;left:172px;top:410px;width:96px;height:36px;border:2px solid var(--white);font-size:11px;font-weight:700;display:flex;align-items:center;justify-content:center}
.info{position:absolute;width:100%;font-size:11px}
</style>
</head>
<body>

<!-- flattened presentation area -->
<div class="abs stage"></div>
<div class="abs stage-name">MIREL VOSS</div>
<div class="abs mini-hero">
  <div class="abs logo" style="left:50px;top:50px;font-size:13px"><span class="dot" style="width:8px;height:8px"></span>MIREL VOSS</div>
  <div class="abs portrait" role="img" aria-label="Portrait of Mirel Voss, arms crossed" style="left:80px;top:90px;width:170px;height:360px"></div>
  <div class="abs frame" style="left:390px;top:160px;width:170px;height:190px"></div>
  <div class="abs hero-title" style="left:340px;top:232px;width:270px;font-size:34px;background:#6a6a6c">Mirel Voss</div>
  <div class="abs hero-sub" style="left:380px;top:282px;width:190px;font-size:8px;letter-spacing:2px">Content Everything</div>
</div>

<!-- hero -->
<div class="abs hero" role="img" aria-label="Soft background photo of a desk with writing hands"></div>
<div class="abs logo" style="left:160px;top:925px;font-size:22px"><span class="dot"></span>MIREL VOSS</div>
<nav class="abs nav" style="left:516px;top:918px;align-items:center">
  <span>Home</span><span>Who I Am</span><span>What I Do</span><span>How to Reach Me</span><span>Contact Us</span><span class="social" aria-label="Professional network"></span>
</nav>
<div class="abs portrait" role="img" aria-label="Portrait of Mirel Voss in a denim shirt, arms crossed" style="left:170px;top:995px;width:320px;height:500px"></div>
<div class="abs frame" style="left:660px;top:1050px;width:250px;height:280px"></div>
<div class="abs" style="left:600px;top:1140px;width:370px;height:130px;background:#707072"></div>
<div class="abs hero-title" style="left:600px;top:1150px;width:370px">Mirel Voss</div>
<div class="abs hero-sub" style="left:600px;top:1232px;width:370px">Content Everything</div>

<!-- intro -->
<div class="abs intro-photo" role="img" aria-label="Photo of hands typing on a laptop"></div>
<div class="abs intro-card">
  <h2>Aliquam gravida dui metus, sit amet <em>finibus</em> augue</h2>
  <p>Donec elementum eget velit a pharetra. Etiam imperdiet leo vitae sem gravida blandit. Etiam sit amet urna porttitor, mattis est et, sollicitudin felis. Ut viverra orci et enim rutrum rutrum. Aliquam faucibus erat ut nunc eleifend, in ultrices quam lacinia. Praesent et magna et mi pharetra consequat non eu lacus. Morbi bibendum dignissim dolor, vitae eleifend mauris volutpat non. Duis egestas leo lectus, eleifend fringilla ex vulputate quis.</p>
</div>

<div class="abs section-title" style="left:0;top:2128px"><span class="hl">About</span> Us</div>
<div class="abs rule" style="left:568px;top:2174px"></div>

<!-- who I am -->
<div class="abs who-band"></div>
<div class="abs who-photo" role="img" aria-label="Portrait of Mirel Voss in a white blouse"></div>
<div class="abs who-title"><span class="hl">Who</span> Am I</div>
<div class="abs rule" style="left:592px;top:2440px"></div>
<p class="abs who-text">I'm a teacher-turned-techie—a seasoned professional who's passionate about all things content, from content architecture and design, when a product first comes on scene, to writing, editing, and publishing content for delivery to the end user. I have a particular love for user behavior and enjoy opportunities with a mix of tech, creative, and analytics.</p>
<div class="abs arrow-box"><svg width="50" height="50" viewBox="0 0 50 50"><path d="M21 15 L31 25 L21 35" fill="none" stroke="#fff" stroke-width="2.5"/></svg></div>

<!-- experience -->
<div class="abs icon-box" style="left:559px;top:2930px"><svg width="82" height="82"><circle cx="41" cy="41" r="12" fill="#fff"/></svg></div>
<div class="abs section-title" style="left:0;top:3040px"><span class="hl">Exper</span>ience</div>
<div class="abs rule" style="left:568px;top:3086px"></div>
<div class="abs timeline"></div>

<div class="abs role" style="left:300px;top:3170px;width:235px"><span class="hl">Content</span>Manager</div>
<div class="abs step" style="left:572px;top:3165px"><svg width="52" height="52"><rect x="17" y="13" width="18" height="24" fill="none" stroke="#1c1c24" stroke-width="2"/><path d="M21 20h10M21 25h10M21 30h7" stroke="#1c1c24" stroke-width="1.6"/></svg></div>
<div class="abs duties" style="left:668px;top:3172px;width:390px">
• Architect, socialize, &amp; integrate new content management platform within Corvane operations<br>
- Drove content design &amp; tool architecture from inception<br>
- Evaluate the user experience, make recommendations for improvement, perform content audits, &amp; enforce architectural strategy<br>
- Collaborate with partner teams to introduce templated automation solutions which reduce risk &amp; increase efficiencies for the business<br>
- Transition existing publication processes to new production flow<br>
• Produce &amp; manage library of Sales Team training &amp; product videos using the Lernio learning &amp; enablement platform<br>
• Execute on Product Owner deliverables by learning departments' context, gathering requirements, &amp; translating to developers
</div>

<div class="abs duties right" style="left:150px;top:3455px;width:395px">
• Built out complex, high-visibility promotions for Nimbra, Vexa, Quillo, Panely, &amp; virtual reality products<br>
• Referenced Merchandising Manifests to create product bundles, set pricing discounts, &amp; develop category, list, &amp; support pages<br>
• Provided input at weekly meetings to assess tool usability &amp; scenarios<br>
• Selected to be part of a dedicated team for a milestone rollout to a new CMS platform for nearly 100 worldwide markets<br>
• Identified &amp; logged bugs in multiple browsers using specific test cases<br>
• Assisted with production, training, &amp; documentation for six rollouts &amp; weekly releases
</div>
<div class="abs step" style="left:572px;top:3450px"><svg width="52" height="52"><rect x="14" y="16" width="24" height="16" fill="none" stroke="#1c1c24" stroke-width="2"/><path d="M22 36h8M26 32v4" stroke="#1c1c24" stroke-width="2"/></svg></div>
<div class="abs role" style="left:667px;top:3455px;width:233px"><span class="hl">Web</span>Producer 2</div>

<div class="abs role" style="left:278px;top:3700px;width:257px"><span class="hl">Senior</span>Web Publisher</div>
<div class="abs step" style="left:572px;top:3695px"><svg width="52" height="52"><rect x="15" y="14" width="22" height="24" fill="none" stroke="#1c1c24" stroke-width="2"/><rect x="19" y="19" width="14" height="7" fill="#1c1c24"/><path d="M19 30h14" stroke="#1c1c24" stroke-width="1.6"/></svg></div>
<div class="abs duties" style="left:668px;top:3705px;width:390px">
• Launched the re-design of the Telvora B2B small business site<br>
- Migrated entire small business site to an upgraded CMS<br>
- Referenced redlines, wireframes, &amp; copy to implement designs<br>
- Deployed XML files to multiple staging &amp; production environments<br>
- Resolved defects reported through test scripts<br>
• Partnered closely with Content, Design, Marketing, Catalog, &amp; Producer teams to code &amp; publish content for 7.7M unique visitors<br>
• Edited &amp; deployed content from an available 4,000 JSP files, 1,500 PDFs, &amp; nearly 12,000 images<br>
• Successfully deployed more than 250 pages for Telvora's highly trafficked help &amp; support microsite (FAQs, user guides, tutorials)
</div>

<!-- testimonials -->
<div class="abs voices"></div>
<div class="abs icon-box" style="left:559px;top:3985px;background:var(--white);width:82px;height:80px"><svg width="82" height="80"><circle cx="41" cy="40" r="12" fill="#151428"/></svg></div>
<div class="abs voices-title">What People Are Saying</div>
<div class="abs rule" style="left:568px;top:4146px;background:var(--white)"></div>

<div class="abs card dim" style="left:117px">Wanted to give a shout out to Mirel for always accommodating difficult requests with such grace. The launch video project I just worked on went smoothly because of her. She's very professional and is wonderful to work with.<div class="who">Daria N</div></div>
<div class="abs card lit" style="left:449px">I am amazed at all the work you have accomplished in such a short time! I want to sincerely thank you for your long hours, dedication and ... well, for your attention! Much gratitude!<div class="who">Theo S</div></div>
<div class="abs card dim" style="left:781px">Thanks Mirel, you're the best... one of the most positive and talented people I've encountered here! Keep in touch!<div class="who">Milo M</div></div>
<div class="abs avatar" role="img" aria-label="Photo of Daria N" style="left:234px"></div>
<div class="abs avatar" role="img" aria-label="Photo of Theo S" style="left:566px"></div>
<div class="abs avatar" role="img" aria-label="Photo of Milo M" style="left:898px"></div>
<div class="abs dot on" style="left:572px"></div>
<div class="abs dot" style="left:588px"></div>
<div class="abs dot" style="left:604px"></div>
<div class="abs dot" style="left:620px"></div>

<!-- contact -->
<div class="abs map" role="img" aria-label="Grey street map of the city" style="left:0;width:380px"></div>
<div class="abs map" role="img" aria-label="Grey street map of the city" style="left:820px;width:380px"></div>
<div class="abs contact">
  <div class="abs" style="left:180px;top:6px;width:80px;height:74px;background:var(--white)"><svg width="80" height="74"><circle cx="40" cy="37" r="12" fill="#151428"/></svg></div>
  <h2>Get In Touch</h2>
  <div class="abs rule" style="left:190px;top:170px;width:60px;background:var(--white);height:4px"></div>
  <div class="field sans" style="top:250px">Your Name</div>
  <div class="field sans" style="top:300px">Your Email Address</div>
  <div class="field sans" style="top:350px">Your Budget</div>
  <div class="send">Send</div>
  <svg class="abs" style="left:212px;top:480px" width="16" height="16" viewBox="0 0 16 16"><path d="M3 1h3l1.5 4-2 1.5a9 9 0 0 0 4 4L11 8.5l4 1.5v3c0 1-1 2-2 2C7 15 1 9 1 3c0-1 1-2 2-2z" fill="#fff"/></svg>
  <div class="info" style="top:500px">555.014.2290</div>
  <svg class="abs" style="left:211px;top:536px" width="18" height="13" viewBox="0 0 18 13"><rect width="18" height="13" fill="#fff"/><path d="M0 0l9 7 9-7" fill="none" stroke="#151428" stroke-width="1.5"/></svg>
  <div class="info" style="top:556px">mirel.voss@mailbox.example</div>
  <div class="info" style="top:628px">© Copyright 2020</div>
</div>

</body>
</html>
```